LAW FIRM - RE-DESIGN - (professional, excellence, tradition and innovation)

We are a premier law firm in New South Wales, Australia. We pride ourselves on being cutting edge and up to date in our market.

Our firm formed in 1874 and has a particularly strong tradition within it's geographic footprint. acting for clients over multiple generations. Despite our regional background, our reputation for excellence has enable us to remain highly visible in a large area.

We have invested heavily in ensuring future planning of this business, and do so on a recurring basis. This has lead to a review of our existing web site.

Although serviceable we feel our previous website is out-of-date and not as in touch with the modern market. We are aware that for the emerging clients a web site is often the face of a firm and a failure to hold attention on the first page may fail to capture the client.

We are seeking designs to communicate the core values of professionalism and excellence. At the same time as maintaining traditional country values of honesty, integrity and hard work we strive to embrace changes to the law and technology.

Target Market(s)

Clients of Law Firm

Industry/Entity Type

Law Firm

Coding

Coded - Design and coding required

Number of Pages Required

5+ page

Requirements
Must have
• A strong sense of professionalism and excellence with a careful balance between traditional values and innovation.
Nice to have
• We have included within our design brief links to top competitors sites to assist for design concepts.

```html
<!DOCTYPE html>
<html lang="en">
<head>
<meta charset="utf-8">
<title>Harwood Law</title>
<link href="https://fonts.googleapis.com/css2?family=Playfair+Display:wght@400;700&family=Open+Sans:wght@400;600&display=swap" rel="stylesheet">
<style>
:root{
  --navy:#0f3f80;
  --navy-deep:#0b2f63;
  --blue:#1a56a6;
  --ink:#2b2b2b;
  --muted:#9a9a9a;
  --line:#e2e2e2;
  --paper:#ffffff;
  --foot:#f3f4f6;
}
*{box-sizing:border-box;margin:0;padding:0}
html,body{width:1200px;height:3409px;overflow:hidden;background:var(--paper)}
body{font-family:"Open Sans",Arial,sans-serif;color:var(--ink);position:relative}
.serif{font-family:"Playfair Display",Georgia,serif}
section,header,footer,.topbar{position:absolute;left:0;width:1200px}

.topbar{top:0;height:36px;background:var(--navy-deep);color:#fff;font-size:12px}
.topbar .contact{position:absolute;left:132px;top:10px;display:flex;gap:26px;align-items:center}
.topbar .contact span{display:flex;gap:8px;align-items:center}
.topbar .social{position:absolute;right:132px;top:12px;display:flex;gap:10px}
.topbar .social i{display:block;width:10px;height:10px;border-radius:2px;background:#fff;opacity:.85}

.site-header{top:36px;height:105px;background:#fff;border-bottom:1px solid var(--line)}
.brand{position:absolute;left:132px;top:30px;display:flex;align-items:center;gap:10px;font-family:"Playfair Display",Georgia,serif;font-size:28px;color:var(--navy);font-weight:700;white-space:nowrap}
.brand .mark{width:16px;height:16px;background:var(--navy)}
.nav{position:absolute;right:132px;top:0;height:105px;display:flex;gap:46px;align-items:center;font-family:"Playfair Display",Georgia,serif;font-size:13px;color:var(--ink)}
.nav a{position:relative;height:105px;display:flex;align-items:center;gap:6px;text-decoration:none;color:inherit}
.nav a.active{color:var(--blue)}
.nav a.active::after{content:"";position:absolute;left:-6px;right:-6px;bottom:-1px;height:4px;background:var(--blue)}
.nav .caret{width:0;height:0;border-left:4px solid transparent;border-right:4px solid transparent;border-top:5px solid currentColor}

.hero{top:141px;height:473px;background:linear-gradient(90deg,#3f4a55 0%,#6f7880 40%,#59626b 62%,#2a3038 80%,#1b1f25 100%);color:#fff}
.hero h1{position:absolute;left:132px;top:140px;font-weight:400;font-size:38px}
.hero p{position:absolute;left:132px;top:215px;width:530px;font-size:12px;line-height:1.9}
.btn{display:inline-flex;align-items:center;justify-content:center;background:var(--navy);color:#fff;font-family:"Playfair Display",Georgia,serif;font-size:13px;border-radius:3px;text-decoration:none}
.hero .btn{position:absolute;left:132px;top:291px;width:164px;height:46px;font-size:14px;box-shadow:0 2px 0 #0a2a55}
.hero .dots{position:absolute;left:134px;top:378px;display:flex;gap:6px}
.hero .dots i{width:10px;height:10px;border-radius:50%;background:#fff}

.welcome{top:614px;height:413px}
.welcome h2{position:absolute;left:132px;top:62px;font-size:31px;font-weight:400;color:var(--navy)}
.welcome p{position:absolute;left:132px;top:123px;width:448px;font-size:10.5px;line-height:2.05;color:var(--muted)}
.welcome .btn{position:absolute;left:132px;top:288px;width:123px;height:41px}
.video{position:absolute;left:620px;top:61px;width:448px;height:268px;background:linear-gradient(135deg,#4a3a2c,#1e1a17 55%,#6b4e30);overflow:hidden}
.video .bar{position:absolute;left:0;right:0;bottom:0;height:34px;background:rgba(0,0,0,.75)}
.video .bar .track{position:absolute;left:62px;right:130px;top:15px;height:4px;background:#777}
.video .bar .play{position:absolute;left:22px;top:10px;width:0;height:0;border-top:7px solid transparent;border-bottom:7px solid transparent;border-left:12px solid #fff}
.video .side{position:absolute;right:8px;top:8px;display:flex;flex-direction:column;gap:6px}
.video .side i{width:28px;height:26px;background:rgba(0,0,0,.7)}
.rule{position:absolute;top:1027px;left:132px;width:936px;height:1px;background:var(--line)}

.practice{top:1028px;height:568px}
.section-title{position:absolute;left:0;width:1200px;text-align:center;font-family:"Playfair Display",Georgia,serif;font-weight:400;font-size:31px;color:var(--navy)}
.practice .section-title{top:57px}
.card{position:absolute;top:142px;width:302px;height:367px;border:1px solid var(--line);text-align:center;background:#fff}
.card .icon{width:86px;height:86px;border-radius:50%;background:var(--navy);margin:34px auto 0;display:flex;align-items:center;justify-content:center}
.card h3{margin-top:24px;font-family:"Playfair Display",Georgia,serif;font-weight:400;font-size:18px}
.card p{margin:20px auto 0;width:250px;font-size:10.5px;line-height:2.05;color:var(--muted)}
.card .btn{position:absolute;left:50%;transform:translateX(-50%);bottom:46px;width:106px;height:37px}
.arrow{position:absolute;width:20px;height:44px}

.faq{top:1596px;height:491px;background:linear-gradient(180deg,#1b5aa8 0%,#104894 45%,#0a3474 100%);color:#fff}
.faq .section-title{top:50px;color:#fff}
.faq-item{position:absolute;left:137px;width:930px;font-family:"Playfair Display",Georgia,serif;font-size:18px}
.faq-item .toggle{position:absolute;right:0;top:4px;width:15px;height:15px;border:1.5px solid #fff;border-radius:2px}
.faq-item .toggle::before{content:"";position:absolute;left:2px;right:2px;top:5px;height:1.5px;background:#fff}
.faq-item .toggle.plus::after{content:"";position:absolute;top:2px;bottom:2px;left:5.3px;width:1.5px;background:#fff}
.faq .answer{position:absolute;left:137px;top:196px;width:930px;font-size:10.5px;line-height:2.2}

.people{top:2087px;height:670px}
.people .section-title{top:64px}
.person{position:absolute;top:150px;width:221px;height:463px;border:1px solid var(--line);text-align:center}
.person .photo{height:218px;background:linear-gradient(160deg,#8a6a45,#3b2b1e)}
.person h3{margin-top:30px;font-family:"Playfair Display",Georgia,serif;font-weight:400;font-size:17px}
.person p{margin:14px auto 0;width:180px;font-size:10.5px;line-height:2;color:var(--muted)}
.person .btn{position:absolute;left:50%;transform:translateX(-50%);bottom:32px;width:109px;height:36px}

.map{top:2757px;height:323px;background:linear-gradient(135deg,#cfd3cf,#bfc5c0 50%,#d6d8d2)}

.site-footer{top:3080px;height:277px;background:var(--foot)}
.site-footer .brand{top:60px;font-size:24px}
.foot-social{position:absolute;left:132px;top:155px;display:flex;gap:7px}
.foot-social i{width:29px;height:29px;border:1.5px solid #666;border-radius:50%}
.col{position:absolute;top:58px;font-size:10px;color:#555}
.col h4{font-family:"Playfair Display",Georgia,serif;font-weight:700;font-size:12px;color:var(--ink);margin-bottom:22px}
.links li{list-style:none;line-height:25px}
.row{display:flex;gap:10px;align-items:flex-start;height:26px;line-height:1.4;white-space:nowrap}
.row svg{flex:none;margin-top:2px}
.row u{text-decoration:underline}
.copy{position:absolute;top:3357px;left:0;width:1200px;height:52px;border-top:1px solid #ddd;background:var(--foot);text-align:center;font-size:9.5px;color:#666;padding-top:22px}
</style>
</head>
<body>

<div class="topbar">
  <div class="contact">
    <span><svg width="11" height="11" viewBox="0 0 24 24"><path fill="#fff" d="M6.6 10.8a15 15 0 006.6 6.6l2.2-2.2a1 1 0 011-.25 11.4 11.4 0 003.6.57 1 1 0 011 1V20a1 1 0 01-1 1A17 17 0 013 4a1 1 0 011-1h3.5a1 1 0 011 1c0 1.25.2 2.45.57 3.6a1 1 0 01-.25 1z"/></svg>555-014-2290</span>
    <span><svg width="12" height="10" viewBox="0 0 24 18"><rect x="1" y="1" width="22" height="16" fill="none" stroke="#fff" stroke-width="2"/><path d="M1 1l11 9 11-9" fill="none" stroke="#fff" stroke-width="2"/></svg>hello@harwoodlaw.example</span>
  </div>
  <div class="social"><i></i><i></i><i></i><i></i></div>
</div>

<header class="site-header">
  <div class="brand"><span class="mark"></span>Harwood Law</div>
  <nav class="nav">
    <a class="active">Home</a>
    <a>About us <span class="caret"></span></a>
    <a>Practice Areas <span class="caret"></span></a>
    <a>People <span class="caret"></span></a>
    <a>Testimonials</a>
    <a>FAQ</a>
    <a>Contact us</a>
  </nav>
</header>

<section class="hero" role="img" aria-label="Photo of a lawyer in a dark suit standing in a boardroom">
  <h1 class="serif">We are a premier law firm</h1>
  <p>We employ highly competent people with a wide range of skills. Our team of both Professional and Support Staff</p>
  <a class="btn">Read More</a>
  <div class="dots"><i></i><i></i><i></i></div>
</section>

<section class="welcome">
  <h2 class="serif">Welcome to Harwood Law</h2>
  <p>Harwood Law has been in existence since 1874, first practising as a single office serving the surrounding district. Over the decades the firm grew through careful mergers and new partners, adding offices in neighbouring towns. In later years the practice expanded again, taking over the work of a long-standing local firm and its clients.</p>
  <a class="btn">Read More</a>
  <div class="video" role="img" aria-label="Video still of a lawyer signing papers beside a gavel">
    <div class="side"><i></i><i></i><i></i><i></i></div>
    <div class="bar"><span class="play"></span><span class="track"></span></div>
  </div>
</section>
<div class="rule"></div>

<section class="practice">
  <h2 class="section-title">Practice areas</h2>
  <svg class="arrow" style="left:84px;top:298px" viewBox="0 0 20 44"><path d="M18 2L2 22l16 20" fill="none" stroke="#ccc" stroke-width="2"/></svg>
  <svg class="arrow" style="left:1097px;top:298px" viewBox="0 0 20 44"><path d="M2 2l16 20L2 42" fill="none" stroke="#ccc" stroke-width="2"/></svg>

  <div class="card" style="left:132px">
    <div class="icon"><svg width="30" height="38" viewBox="0 0 30 38"><rect x="2" y="2" width="26" height="34" fill="#fff"/><g fill="#0f3f80"><rect x="7" y="7" width="4" height="4"/><rect x="13" y="7" width="4" height="4"/><rect x="19" y="7" width="4" height="4"/><rect x="7" y="14" width="4" height="4"/><rect x="13" y="14" width="4" height="4"/><rect x="19" y="14" width="4" height="4"/><rect x="7" y="21" width="4" height="4"/><rect x="13" y="21" width="4" height="4"/><rect x="19" y="21" width="4" height="4"/><rect x="12" y="28" width="6" height="8"/></g></svg></div>
    <h3>Construction</h3>
    <p>Although not essential, it is recommended that designers review the above-mentioned links which may provide an indication.</p>
    <a class="btn">Read More</a>
  </div>
  <div class="card" style="left:448px">
    <div class="icon"><svg width="40" height="40" viewBox="0 0 40 40"><path fill="#fff" d="M10 14l3-10h14l3 10zM5 15h30v3H5zM8 38c0-9 5-14 12-14s12 5 12 14z"/><circle cx="20" cy="21" r="3" fill="#fff"/></svg></div>
    <h3>Criminal</h3>
    <p>Although not essential, it is recommended that designers review the above-mentioned links which may provide an indication.</p>
    <a class="btn">Read More</a>
  </div>
  <div class="card" style="left:766px">
    <div class="icon"><svg width="46" height="34" viewBox="0 0 46 34"><g fill="#fff"><circle cx="23" cy="8" r="6"/><circle cx="9" cy="11" r="4.5"/><circle cx="37" cy="11" r="4.5"/><path d="M13 32c0-9 4-14 10-14s10 5 10 14z"/><path d="M1 30c0-7 3-11 8-11 2 0 3 .5 4 1.2-1.4 2.7-2 6-2 9.8z"/><path d="M45 30c0-7-3-11-8-11-2 0-3 .5-4 1.2 1.4 2.7 2 6 2 9.8z"/></g></svg></div>
    <h3>Family</h3>
    <p>Although not essential, it is recommended that designers review the above-mentioned links which may provide an indication.</p>
    <a class="btn">Read More</a>
  </div>
</section>

<section class="faq">
  <h2 class="section-title">FAQ</h2>
  <div class="faq-item" style="top:148px">Harwood Law is proud to support and be part of these great community events and programs<span class="toggle"></span></div>
  <p class="answer">We offer a range of legal services throughout the Highland Region and beyond. It is our firm's policy to refer clients to the person within the firm that has the necessary expertise to gain the best outcome for their particular matter. If necessary we have contact with a number of Barristers if a matter needs further expert opinion.</p>
  <div class="faq-item" style="top:273px">Our team of both Professional and Support Staff have many years of experience<span class="toggle plus"></span></div>
  <div class="faq-item" style="top:314px">our team has a real commitment to the firm and its clients.<span class="toggle plus"></span></div>
  <div class="faq-item" style="top:360px">We value an open and honest approach to all client service, ensuring the highest level of communication<span class="toggle plus"></span></div>
</section>

<section class="people">
  <h2 class="section-title">Our People</h2>
  <svg class="arrow" style="left:84px;top:356px" viewBox="0 0 20 44"><path d="M18 2L2 22l16 20" fill="none" stroke="#ccc" stroke-width="2"/></svg>
  <svg class="arrow" style="left:1097px;top:356px" viewBox="0 0 20 44"><path d="M2 2l16 20L2 42" fill="none" stroke="#ccc" stroke-width="2"/></svg>
  <div class="person" style="left:132px"><div class="photo" role="img" aria-label="Portrait of Owen Hartley in front of law books"></div><h3>Owen Hartley</h3><p>Nemo enim ipsam voluptatem quia voluptas sit aspernatur aut odit aut fugit, sed quia consequuntur magni dolores eos</p><a class="btn">Read More</a></div>
  <div class="person" style="left:370px"><div class="photo" role="img" aria-label="Portrait of Clara Whitmore in front of law books"></div><h3>Clara Whitmore</h3><p>Nemo enim ipsam voluptatem quia voluptas sit aspernatur aut odit aut fugit, sed quia consequuntur magni dolores eos</p><a class="btn">Read More</a></div>
  <div class="person" style="left:607px"><div class="photo" role="img" aria-label="Portrait of Rosalind Ashby in front of law books"></div><h3>Rosalind Ashby</h3><p>Nemo enim ipsam voluptatem quia voluptas sit aspernatur aut odit aut fugit, sed quia consequuntur magni dolores eos</p><a class="btn">Read More</a></div>
  <div class="person" style="left:843px"><div class="photo" role="img" aria-label="Portrait of Martin Leung in front of law books"></div><h3>Martin Leung</h3><p>Nemo enim ipsam voluptatem quia voluptas sit aspernatur aut odit aut fugit, sed quia consequuntur magni dolores eos</p><a class="btn">Read More</a></div>
</section>

<section class="map" role="img" aria-label="Street map showing the firm's office location"></section>

<footer class="site-footer">
  <div class="brand"><span class="mark"></span>Harwood Law</div>
  <div class="foot-social"><i></i><i></i><i></i><i></i><i></i></div>

  <div class="col" style="left:366px">
    <h4>Quick Links</h4>
    <ul class="links"><li>Home</li><li>About Us</li><li>Services</li><li>People</li><li>Community</li><li>FAQ</li><li>Contact us</li></ul>
  </div>

  <div class="col" style="left:539px">
    <h4>NORTHVALE</h4>
    <div class="row"><svg width="11" height="10" viewBox="0 0 11 10"><rect width="11" height="10" rx="1" fill="#555"/></svg>02 5550 7182</div>
    <div class="row"><svg width="11" height="10" viewBox="0 0 11 10"><rect width="11" height="10" rx="1" fill="#555"/></svg>02 5550 7196</div>
    <div class="row"><svg width="11" height="9" viewBox="0 0 11 9"><rect width="11" height="9" fill="#555"/><path d="M0 0l5.5 5L11 0" stroke="#fff" fill="none"/></svg><u>hello@harwoodlaw.example</u></div>
    <div class="row"><svg width="9" height="12" viewBox="0 0 9 12"><path d="M4.5 0A4.5 4.5 0 000 4.5C0 8 4.5 12 4.5 12S9 8 9 4.5A4.5 4.5 0 004.5 0z" fill="#555"/></svg><span>Suite 9, Market Arcade<br>Northvale 2861</span></div>
  </div>

  <div class="col" style="left:745px">
    <h4>EASTBROOK</h4>
    <div class="row"><svg width="11" height="10" viewBox="0 0 11 10"><rect width="11" height="10" rx="1" fill="#555"/></svg>02 5551 3804</div>
    <div class="row"><svg width="11" height="10" viewBox="0 0 11 10"><rect width="11" height="10" rx="1" fill="#555"/></svg>02 5551 3817</div>
    <div class="row"><svg width="11" height="9" viewBox="0 0 11 9"><rect width="11" height="9" fill="#555"/><path d="M0 0l5.5 5L11 0" stroke="#fff" fill="none"/></svg><u>hello@harwoodlaw.example</u></div>
    <div class="row"><svg width="9" height="12" viewBox="0 0 9 12"><path d="M4.5 0A4.5 4.5 0 000 4.5C0 8 4.5 12 4.5 12S9 8 9 4.5A4.5 4.5 0 004.5 0z" fill="#555"/></svg><span>118 Ridge Street<br>Eastbrook 2874</span></div>
  </div>

  <div class="col" style="left:939px">
    <h4>WESTMERE</h4>
    <div class="row"><svg width="11" height="10" viewBox="0 0 11 10"><rect width="11" height="10" rx="1" fill="#555"/></svg>02 5552 9031</div>
    <div class="row"><svg width="11" height="10" viewBox="0 0 11 10"><rect width="11" height="10" rx="1" fill="#555"/></svg>02 5552 9048</div>
    <div class="row"><svg width="11" height="9" viewBox="0 0 11 9"><rect width="11" height="9" fill="#555"/><path d="M0 0l5.5 5L11 0" stroke="#fff" fill="none"/></svg><u>hello@harwoodlaw.example</u></div>
    <div class="row"><svg width="9" height="12" viewBox="0 0 9 12"><path d="M4.5 0A4.5 4.5 0 000 4.5C0 8 4.5 12 4.5 12S9 8 9 4.5A4.5 4.5 0 004.5 0z" fill="#555"/></svg><span>74 Fielder Street<br>Westmere 2893</span></div>
  </div>
</footer>
<div class="copy">©2017 Harwood Law . All rights reserved.</div>

</body>
</html>
```